Coaching Workbook (for life & health coaching industry)

I created a coaching workbook using Canva. I would like it recreated more professionally in PowerPoint with better images and creative design using my 3 branding colors (teal primary, salmon secondary, and turquoise splash here and there).

Please use the attached image of lady sitting on dock at the lake on the first slide for the cover along with my logo and my titles (similar to my Canva version on my website).

My version of the workbook is attached. Thank you for turning my drab into fab:-) Mavis Ketterwell, Life & Health Coach, Grief Recovery Specialist
Updates

To ensure clarity, I am looking for a PowerPoint (prefer vertical format) for a coaching manual FROM the material in the version that I created in Canva, which is currently on my website as a download at the bottom of my coaching page: https://brightpathwayguide.example/coaching-2 I will upload the pdf file as well as the example that I'm trying to recreate in PowerPoint, but more professionally and creatively. Thank You! Mavis Ketterwell

Target Market(s)

My target audience is primarily female, with a few males each year, ages range from mid-twenties to sixties. Everyone will experience the pain of loss and grief. Women are more prone to reach out for help sooner.

Industry/Entity Type

Life Coaching

Font styles to use
Serif

Requirements
Must have
• Want it to feel personal, not corporate if that makes sense.
• Must use my 3 branding colors: HEX # 2994ae, 10dfd3, fa8070.
• Please use Playfair Display font for consistency with my website.
• The text for the workbook is included in the Word document attached below.
Should not have
• I'm not looking for the material on my website to be the focus of this workbook. I want the Canva version that I created to be converted more professionally and creatively in PowerPoint, so I can manage moving forward.

```html
<!DOCTYPE html>
<html lang="en">
<head>
<meta charset="utf-8">
<title>Bright Pathway Coaching Workbook</title>
<link rel="stylesheet" href="https://fonts.googleapis.com/css2?family=Playfair+Display:ital,wght@0,400;0,700;0,900;1,400;1,700&family=Noto+Serif:wght@400&display=swap">
<style>
  :root {
    --teal: #2994ae;
    --salmon: #fa8070;
    --turquoise: #10dfd3;
    --ink: #1e1e1e;
    --paper: #ffffff;
    --backdrop: #ececec;
    --heading: "Playfair Display", Georgia, serif;
    --body: "Noto Serif", Georgia, serif;
  }
  * { box-sizing: border-box; margin: 0; padding: 0; }
  html, body { width: 1200px; height: 2250px; overflow: hidden; background: var(--backdrop); }
  .spread { position: relative; width: 1200px; height: 2250px; }
  .page {
    position: absolute; width: 535px; height: 745px; background: var(--paper);
    overflow: hidden; box-shadow: 0 1px 4px rgba(0,0,0,.18);
  }
  .col-left { left: 36px; }
  .col-right { left: 584px; }
  .row-1 { top: 0; }
  .row-2 { top: 751px; }
  .row-3 { top: 1502px; }
  .block { position: absolute; }
  .photo { position: absolute; }
  .teal-panel { position: absolute; background: var(--teal); }
  .section-label {
    position: absolute; background: var(--paper); display: flex; align-items: center; justify-content: center;
    font-family: var(--heading); font-weight: 700; letter-spacing: 2.5px; color: var(--ink); font-size: 20px;
  }
  .copy {
    position: absolute; color: #fff; font-family: var(--body); font-size: 11px; line-height: 1.36;
    text-align: justify;
  }
  .copy p { margin-bottom: 7px; }
  .copy a { color: #fff; text-decoration: underline; }
  .callout {
    position: absolute; font-family: var(--heading); font-weight: 700; color: var(--salmon);
    font-size: 15px; line-height: 1.35;
  }

  /* cover */
  .cover-title {
    left: 208px; top: 0; width: 306px; height: 293px; background: var(--teal);
    color: #fff; font-family: var(--heading); font-weight: 700; font-size: 27px; line-height: 1.5;
    letter-spacing: 1px; text-align: center; display: flex; align-items: center; justify-content: center; padding-top: 10px;
  }
  .cover-name {
    left: 33px; top: 510px; width: 306px; height: 120px; background: var(--salmon); color: #fff;
    font-family: var(--heading); padding: 36px 0 0 36px;
  }
  .cover-name .name { font-size: 17px; letter-spacing: 3px; font-weight: 700; }
  .cover-name .role { font-size: 10.5px; letter-spacing: 1.5px; font-weight: 700; margin-top: 4px; padding-left: 16px; line-height: 1.55; }
  .cover-tagline {
    left: 0; width: 535px; top: 660px; text-align: center; color: var(--teal);
    font-family: var(--heading); font-style: italic; font-weight: 700; font-size: 25px; letter-spacing: .8px;
  }

  /* contents */
  .contents-rule { left: 0; top: 0; width: 9px; height: 745px; background: var(--teal); }
  .contents-title {
    left: 76px; top: 118px; color: var(--teal); font-family: var(--heading); font-weight: 700;
    font-size: 33px; line-height: 1.15; letter-spacing: .5px;
  }
  .contents-list { left: 76px; top: 228px; width: 252px; list-style: none; }
  .contents-list li {
    display: flex; height: 35px; align-items: center; border-bottom: 1.5px solid var(--teal);
    font-family: var(--body); font-size: 11.5px; color: var(--ink);
  }
  .contents-list .num { width: 46px; text-align: center; color: var(--teal); font-family: var(--heading); font-size: 13px; }

  /* welcome */
  .welcome-head { left: 35px; top: 55px; width: 476px; height: 65px; justify-content: flex-start; padding-left: 33px; font-size: 19px; line-height: 1.35; }
  .welcome-sign { left: 24px; top: 636px; font-family: var(--heading); }
  .welcome-sign .name { color: var(--salmon); font-style: italic; font-weight: 700; font-size: 24px; }
  .welcome-sign .role { font-family: var(--body); font-size: 11px; color: var(--ink); line-height: 1.35; margin-top: 6px; }
</style>
</head>
<body>
<main class="spread">

  <!-- cover -->
  <section class="page col-left row-1">
    <div class="photo" style="left:0;top:120px;width:535px;height:447px;background:linear-gradient(180deg,#b9c7d2 0%,#8aa0a8 38%,#5e7a78 55%,#a7b8c6 70%,#6e8596 100%);" role="img" aria-label="Woman sitting at the end of a wooden dock on a calm mountain lake, pine tree on the left"></div>
    <div class="block cover-title">BRIGHT PATHWAY<br>COACHING<br>WORKBOOK</div>
    <div class="block cover-name">
      <div class="name">MAVIS KETTERWELL</div>
      <div class="role">LIFE&amp;HEALTH COACH<br>GRIEFRECOVERY SPECIALIST</div>
    </div>
    <div class="block cover-tagline">Experience your full potential for joy</div>
  </section>

  <!-- contents -->
  <section class="page col-right row-1">
    <div class="block contents-rule"></div>
    <h1 class="block contents-title">TABLE OF<br>CONTENTS</h1>
    <ol class="block contents-list">
      <li><span class="num">1</span>Welcome Message</li>
      <li><span class="num">2</span>Benefits of Journaling</li>
      <li><span class="num">3</span>Life Satisfaction</li>
      <li><span class="num">4</span>Understand Your Why</li>
      <li><span class="num">5</span>Values &amp; Beliefs</li>
      <li><span class="num">6</span>Personal Mission Statement</li>
      <li><span class="num">7</span>SMART Goals</li>
      <li><span class="num">8</span>What Are You Tolerating?</li>
      <li><span class="num">9</span>You Are Enough!</li>
      <li><span class="num">10</span>Sample Worksheet</li>
      <li><span class="num">11</span>Coaching Model</li>
      <li><span class="num">12</span>Reflection</li>
    </ol>
  </section>

  <!-- welcome -->
  <section class="page col-left row-2">
    <div class="photo" style="left:24px;top:30px;width:241px;height:535px;background:linear-gradient(180deg,#9c93c4 0%,#e9b7a8 35%,#f4c98e 55%,#8e6a4f 80%,#4b3a2c 100%);" role="img" aria-label="Silhouette of a woman stretching her arm to the sky in a meadow at sunset"></div>
    <div class="section-label welcome-head">Congratulations on taking the first<br>step to a healthier emotional life!</div>
    <div class="teal-panel" style="left:243px;top:156px;width:268px;height:560px;"></div>
    <div class="copy" style="left:264px;top:220px;width:228px;height:480px;">
      <p>This workbook gives an overview of the transformational exercises I incorporate during our coaching sessions. Skim through these pages to get an idea of what it's like working with me.</p>
      <p>As your coach, I'll be your support and guide as you find the focus and strength to make changes to your life. It'll be hard work, but I'll be there with you every step of the way.</p>
      <p>My goal is to empower you to confront the "sticky stuff." That is, those unpleasant memories, unwanted negative emotions, or secret insecurities. The areas most of us are uncomfortable talking about. The areas that most often keep us stuck.</p>
      <p>My life and health coaching packages are available to improve your life in several areas, like mindfulness, healthy habits, relationships, and goal setting.</p>
      <p>Client Corner becomes your online library, filled with years of personal and professional development resources to apply to your own life.</p>
      <p>One new thought can change the direction of your life! Schedule a complimentary discovery coaching session and let's get you living your best life.</p>
    </div>
    <div class="block welcome-sign">
      <div class="name">Mavis Ketterwell</div>
      <div class="role">Life &amp; Health Coach<br>Grief Recovery Specialist</div>
    </div>
  </section>

  <!-- understand your why -->
  <section class="page col-right row-2">
    <div class="teal-panel" style="left:202px;top:54px;width:292px;height:642px;"></div>
    <div class="photo" style="left:55px;top:99px;width:312px;height:377px;background:linear-gradient(180deg,#c4cfd8 0%,#8fa3a6 40%,#5f7a74 58%,#9fb1bf 75%,#6a8192 100%);" role="img" aria-label="Woman sitting on a wooden dock over a mountain lake"></div>
    <div class="section-label" style="left:138px;top:189px;width:330px;height:53px;">Understand Your Why</div>
    <div class="copy" style="left:214px;top:485px;width:268px;">
      <p>Cognitive clarity means understanding your why. Learning what motivates you and influences your decisions and actions is not only key to making successful life changes, it's also what gives you an idea of what makes you tick and why.</p>
      <p>Our brains are gifted with the ability to make new and improved neural pathways throughout our life. My goal as your coach is to help you connect with your why on a deeper level and foster healthier connections as you continue working on your goals.</p>
      <p><a href="https://brightpathwayguide.example/coaching-2">Read more about understanding your why.</a></p>
    </div>
    <div class="callout" style="left:36px;top:553px;width:152px;text-align:right;">Cognitive clarity is an integral component of getting the most out of life coaching!</div>
  </section>

  <!-- values & beliefs -->
  <section class="page col-left row-3">
    <div class="teal-panel" style="left:0;top:55px;width:222px;height:690px;"></div>
    <div class="photo" style="left:222px;top:0;width:313px;height:600px;background:linear-gradient(160deg,#6fa1c2 0%,#e7c2ad 35%,#f1cdb6 55%,#5f8fb0 100%);" role="img" aria-label="Adult and child hands cupped together holding a red heart over blue wooden boards"></div>
    <div class="section-label" style="left:78px;top:113px;width:330px;height:52px;">Values &amp; Beliefs</div>
    <div class="copy" style="left:24px;top:199px;width:184px;font-size:10.4px;line-height:1.33;">
      <p>Our values and beliefs are what drive the direction of your life. Yet, most people never stop to seriously consider what their values and beliefs are.</p>
      <p>That's why so many of us find ourselves wondering, "How did I get here?"</p>
      <p>Upon reflection, you may find that you've modeled your values and beliefs after those of the important people in your life, like your parents. Or, you may find that as you move through life, your values and beliefs changed.</p>
      <p>Unfortunately, it's possible you'll also discover you've been holding onto negative beliefs about yourself for years. Life coaching shines a bright light on where and how some of our negative belief patterns were adopted. Reversing any <a href="https://brightpathwayguide.example/coaching-2">negative core beliefs</a> affecting your life will be instrumental in our work together.</p>
      <p>Once you know clearly your values and beliefs, it'll be easier to be the person you want to be in all circumstances. And as you work to achieve your goals, you'll make decisions that are closely aligned with <a href="https://brightpathwayguide.example/coaching-2">your core values</a>. Ultimately, you'll feel like you're completely living a life of integrity.</p>
    </div>
    <div class="callout" style="left:300px;top:652px;width:210px;text-align:right;">What are your deepest held values and beliefs?</div>
  </section>

  <!-- personal mission statement -->
  <section class="page col-right row-3">
    <div class="photo" style="left:35px;top:48px;width:356px;height:427px;background:linear-gradient(180deg,#f3d6b7 0%,#e2a06e 35%,#a8643d 65%,#5d3826 100%);" role="img" aria-label="Hiker standing on a rocky cliff edge above a hazy canyon at sunrise"></div>
    <div class="teal-panel" style="left:81px;top:258px;width:418px;height:452px;"></div>
    <div class="section-label" style="left:73px;top:315px;width:392px;height:54px;">Personal Mission Statement</div>
    <div class="copy" style="left:100px;top:484px;width:382px;font-size:10.4px;line-height:1.33;">
      <p>Corporations have mission statements to inform the direction of their business decisions. Similarly, personal mission statements help us manage the direction of our lives.</p>
      <p>When we don't know where we want to go, how will we know how to get there? Your personal mission statement will help you live the life you most desire. It will become your compass, directing every decision. You'll be able to stay on course easier knowing what you are working towards.</p>
      <p>Every decision, relationship, promotion, and expenditure can be weighed against your personal mission statement. Before acting, you can ask, "Will this next step bring me closer to or further away from my mission?" And have a crystal clear answer.</p>
      <p><a href="https://brightpathwayguide.example/coaching-2">Read How To Write A Personal Mission Statement In 8 Steps</a></p>
    </div>
  </section>

</main>
</body>
</html>
```